Personal Injury Book Ad Photo Set

I need a series of images for a Threadloop ad campaign for promoting a book titled "Making Sense of an Accident Claim".

```html
<!DOCTYPE html>
<html lang="en">
<head>
<meta charset="utf-8">
<title>Making Sense of an Accident Claim — Book Cover</title>
<link rel="stylesheet" href="https://fonts.googleapis.com/css2?family=Bebas+Neue&display=swap">
<style>
  :root {
    --backdrop: #3a2b22;
    --cover-light: #eef0f3;
    --cover-mid: #d9dde3;
    --panel-top: #85735e;
    --panel-bottom: #b2a792;
    --title: #f4f2ee;
    --art-light: #c9bcb0;
    --art-dark: #7a5e4b;
  }
  * { margin: 0; padding: 0; box-sizing: border-box; }
  html, body {
    width: 1200px;
    height: 960px;
    overflow: hidden;
    background: var(--backdrop);
  }
  .canvas {
    position: relative;
    width: 1200px;
    height: 960px;
  }
  .book-cover {
    position: absolute;
    left: 320px;
    top: 72px;
    width: 560px;
    height: 815px;
    overflow: hidden;
    background: radial-gradient(ellipse at 30% 40%, var(--cover-light) 0%, var(--cover-mid) 100%);
  }
  .title-panel {
    position: absolute;
    left: 136px;
    top: 126px;
    width: 281px;
    height: 424px;
    background: linear-gradient(180deg, var(--panel-top) 0%, var(--panel-bottom) 100%);
  }
  .book-title {
    position: absolute;
    left: 34px;
    top: 42px;
    width: 215px;
    font-family: 'Bebas Neue', 'Oswald', sans-serif;
    font-weight: 400;
    color: var(--title);
  }
  .book-title .lead {
    display: block;
    font-size: 36px;
    line-height: 37px;
    letter-spacing: 0.5px;
    white-space: nowrap;
  }
  .book-title .key {
    display: block;
    font-size: 110px;
    line-height: 100px;
    letter-spacing: 1px;
    margin-top: 8px;
    white-space: nowrap;
  }
  .gavel-art {
    position: absolute;
    left: 0;
    top: 497px;
    width: 560px;
    height: 318px;
    background: linear-gradient(180deg, var(--art-light) 0%, var(--art-dark) 100%);
  }
</style>
</head>
<body>
  <main class="canvas">
    <section class="book-cover">
      <div class="title-panel">
        <h1 class="book-title">
          <span class="lead">Making Sense</span>
          <span class="lead">of an Accident</span>
          <span class="key">Claim</span>
        </h1>
      </div>
      <div class="gavel-art" role="img" aria-label="Wooden judge's gavel striking down and shattering into flying wood splinters"></div>
    </section>
  </main>
</body>
</html>
```